Creative Typography Posters

I am looking for designers that would be interested in long-term co-operation and this is your chance to express your interest and show what you can deliver.

The task:
Choose any 10 quotes from the list and create 10 unique and original posters as per the specification. For easier review, concatenate them into one larger picture - side by side.

Specification:
* 2:3 ratio (portrait) - 1280x1920 pixels per poster
* the poster must be readable even in low resolutions (e.g. 320x480px)
* no copyrighted content (photographs, illustrations, fonts)
* designs that will match the quote/idea visually will be preferred
* be diverse, make each design different and interesting in its own way

Quotes:
* In the beginning there was nothing. God said, 'Let there be light!' And there was light. There was still nothing, but you could see it a whole lot better. -Marla Pettivoss

* Life isn’t about waiting for the storm to pass. It’s about dancing in the rain.

* All I ask is a chance to prove that money can't make me happy.

* The big difference between sex for money and sex for free is that sex for money usually costs a lot less. -Corwin Haldsby

* If you understand what you're doing, you're not learning anything. -T.W.

* To win without risk is to triumph without glory. -Gaston Vireleau

* Love the ones you can. Touch the ones you can reach. Let the others go.

* I would never die for my beliefs because I might be wrong. -Osmund Kettleby

* Never be afraid to do something new. Remember, amateurs built the ark; professionals built the colossa.

* Live as you would have wished to live when you are dying.

* The only way of finding the limits of the possible is by going beyond them into the impossible. -Morris T. Quade

* Feeling resistance means you're moving forward.

* A bottle of wine contains more philosophy than all the books in the world. -Henri Dumolay

* Man prefers to believe what he prefers to be true. -Edwin Marlowe

* If at first you don't succeed, failure may be your style. -Rupert Vanley

* Choose a job you love and you will never have to work a day in your life. -Meng Tavo

* Statisticians do it with 95% confidence.

* Just because no one saw it doesn't mean it didn't happen.

* Life begins at the end of your comfort zone

* And then my sould saw you and it kind of went "Oh there you are. I've been looking for you."

* Sometimes, the people with the worst pasts can create the best futures.

* Women are like the NVK, they already know what you have been up to, they just wait for the right moment to confront you.

Examples:
http://img.plakowave.com/2011/08/letter/2.jpg

http://media2.vexplorin.com/files/2010/10/39/0/1090/10906352/f992956978fe1d58_Red_Ember_v2_by_SirPorcupo.jpg

http://cdn.quibblor.com/wp-content/uploads/2012/03/typographic-poster-1.jpg

http://glimmerfeld.com/wp-content/uploads/2012/03/Typographic-Poster1.jpg

http://glimmerfeld.com/wp-content/uploads/2012/03/Typographic-Poster.jpg

http://data.trovumcdn.com/images/9868837/a0_size_typography_poster_by_lanternmoth47_large.jpg

Now, make art happen!

```html
<!DOCTYPE html>
<html lang="en">
<head>
<meta charset="utf-8">
<title>Let There Be Light — Typographic Poster</title>
<link rel="stylesheet" href="https://fonts.googleapis.com/css2?family=Open+Sans:ital,wght@1,700&display=swap">
<style>
  :root {
    --night: #000000;
    --ink: #ffffff;
    --light: #fff27a;
    --light-core: #ffef6e;
    --glow: rgba(255, 250, 200, 0.55);
    --earth-high: #5e4330;
    --earth-mid: #6f4c33;
    --earth-low: #3b2819;
  }
  * { margin: 0; padding: 0; box-sizing: border-box; }
  html, body {
    width: 800px;
    height: 1200px;
    overflow: hidden;
    background: var(--night);
  }
  .poster {
    position: relative;
    width: 800px;
    height: 1200px;
    overflow: hidden;
    background: var(--night);
    font-family: "Open Sans", Arial, sans-serif;
    font-weight: 700;
    font-style: italic;
    color: var(--ink);
  }
  .landscape {
    position: absolute;
    left: 0;
    top: 560px;
    width: 800px;
    height: 640px;
    background:
      radial-gradient(ellipse 70% 30% at 50% 8%, rgba(120, 110, 100, 0.35), transparent 70%),
      linear-gradient(to bottom,
        rgba(0, 0, 0, 1) 0%,
        rgba(40, 30, 24, 0.9) 10%,
        var(--earth-high) 28%,
        var(--earth-mid) 60%,
        var(--earth-low) 100%);
  }
  .sun {
    position: absolute;
    left: 448px;
    top: 549px;
    width: 0;
    height: 0;
  }
  .sun-glow {
    position: absolute;
    left: -160px;
    top: -160px;
    width: 320px;
    height: 320px;
    border-radius: 50%;
    background: radial-gradient(circle, var(--glow) 0%, rgba(255, 250, 210, 0.25) 40%, transparent 70%);
  }
  .sun-core {
    position: absolute;
    left: -56px;
    top: -56px;
    width: 112px;
    height: 112px;
    border-radius: 50%;
    background: var(--light-core);
    box-shadow: 0 0 24px 8px rgba(255, 245, 170, 0.6);
  }
  .line {
    position: absolute;
    font-size: 40px;
    line-height: 60px;
    letter-spacing: 0.12em;
    white-space: nowrap;
  }
  .line-opening { left: 68px; top: 180px; }
  .line-command { left: 42px; top: 438px; }
  .line-result  { left: 42px; top: 510px; }
  .line-punch   { left: 18px; top: 730px; line-height: 44px; }
  .highlight { color: var(--light); }
  .on-light { color: #1a1a1a; }
</style>
</head>
<body>
  <main class="poster">
    <div class="landscape" role="img" aria-label="Dim rocky desert hills under a dark night sky"></div>

    <div class="sun" aria-hidden="true">
      <div class="sun-glow"></div>
      <div class="sun-core"></div>
    </div>

    <p class="line line-opening">In the beginning there was<br>nothing.</p>
    <p class="line line-command">God said, 'Let there be <span class="highlight">light!'</span></p>
    <p class="line line-result">And there was <span class="on-light">light</span>.</p>
    <p class="line line-punch">There was still nothing, but you<br>could see it a whole lot better</p>
  </main>
</body>
</html>
```